Vintage Style Soup Package Label

I make dry soup packages. I am looking for a label for my soups that shows Quality, Homemade Goodness. Easy, Delicious. My company is called Uncle Barnaby Pantry, But I want this soup line to be called "Thistle & Rye " All my product has a very Vintage Antique look.
I Love Typography. My 6 cup soups are packaged in a flat black bag.
my website is www.unclebarnabypantry.example. I have 15 different Flavours. Our motto is Simple Suppers, Every Day.
While creating the label if you wanted to use
Please use "Chicken Pot Pie" as your sample please and thanks.

Target Market(s)

I want to sell my soups to upscale Grocery and Specialty stores.

Font styles to use
Serif
Sans Serif
Other font styles liked:
• Castellar

Colors
6c449b
ec1f27
ffc214
9ccb3b
ffffff
f37122

Requirements
Must have
• NOTE: A place for weight needs to be on the label

My labels I print on are Vertical 3.33 x4"
Colours. I do not like Pink or Pastel colours. I prefer Dark or grunge colours.
Nice to have
• NOTE: I live in Canada so my packaging is supposed to have English and French on it. The rule state because I am a small business I do not have to. But if you can figure a way to put in the design that would be fine but not necessary. If you did add it to the design it does not have to be the same size font as the English.
Should not have
• Pastel Colours.

```html
<!DOCTYPE html>
<html lang="en">
<head>
<meta charset="utf-8">
<title>Thistle &amp; Rye – Chicken Pot Pie Label</title>
<link rel="stylesheet" href="https://fonts.googleapis.com/css2?family=Cinzel:wght@400;700&family=Rye&display=swap">
<style>
  :root {
    --page: #f3f3f3;
    --charcoal: #2f2f31;
    --charcoal-deep: #222224;
    --gold: #a27b36;
    --gold-dark: #7a5a24;
    --parchment: #caa46a;
    --parchment-light: #d6b57f;
    --ink-brown: #4a2a0e;
    --ink-dark: #2a1606;
    --banner-text: #e9e5dc;
  }
  * { margin: 0; padding: 0; box-sizing: border-box; }
  html, body {
    width: 672px;
    height: 1200px;
    overflow: hidden;
    background: var(--page);
  }
  .canvas {
    position: relative;
    width: 672px;
    height: 1200px;
    display: flex;
    align-items: center;
    justify-content: center;
  }
  .label {
    width: 560px;
    height: 682px;
    display: block;
  }
  .brand-name {
    font-family: "Cinzel", serif;
    font-size: 38px;
    letter-spacing: 2px;
    fill: var(--banner-text);
  }
  .product-title {
    font-family: "Rye", serif;
    fill: var(--ink-brown);
    stroke: var(--ink-dark);
    stroke-width: 2;
  }
  .motto {
    font-family: "Cinzel", serif;
    font-weight: 700;
    font-size: 38px;
    fill: var(--banner-text);
    stroke: var(--charcoal-deep);
    stroke-width: 1.2;
  }
  .weight {
    font-family: "Cinzel", serif;
    font-size: 40px;
    letter-spacing: 1px;
    fill: var(--banner-text);
  }
</style>
</head>
<body>
<main class="canvas">
  <svg class="label" viewBox="0 0 608 740" xmlns="http://www.w3.org/2000/svg" aria-labelledby="label-title">
    <title id="label-title">Thistle &amp; Rye Chicken Pot Pie soup label</title>
    <defs>
      <linearGradient id="ornament-tone" x1="0" y1="0" x2="0" y2="1">
        <stop offset="0" stop-color="#8a6a2e"/>
        <stop offset="1" stop-color="#5e4620"/>
      </linearGradient>
      <radialGradient id="parchment-tone" cx="0.5" cy="0.45" r="0.6">
        <stop offset="0" stop-color="var(--parchment-light)"/>
        <stop offset="1" stop-color="var(--parchment)"/>
      </radialGradient>
      <linearGradient id="bowl-tone" x1="0" y1="0" x2="0" y2="1">
        <stop offset="0" stop-color="#b08a52"/>
        <stop offset="1" stop-color="#8f6a36"/>
      </linearGradient>
      <path id="brand-arc" d="M120 118 Q304 30 500 118"/>
      <path id="weight-arc" d="M140 712 Q300 740 460 690"/>
    </defs>

    <!-- frame -->
    <rect class="label-frame" x="0" y="0" width="608" height="740" fill="var(--gold)"/>
    <rect class="label-field" x="6" y="6" width="596" height="728" fill="var(--charcoal)"/>

    <!-- side scrollwork panels -->
    <rect class="scroll-panel scroll-panel--left" x="14" y="14" width="80" height="712" rx="6"
          fill="url(#ornament-tone)" role="img" aria-label="Vintage scrollwork ornament along the left edge"/>
    <rect class="scroll-panel scroll-panel--right" x="514" y="14" width="80" height="712" rx="6"
          fill="url(#ornament-tone)" role="img" aria-label="Vintage scrollwork ornament along the right edge"/>

    <!-- parchment medallion -->
    <ellipse class="parchment" cx="304" cy="380" rx="302" ry="300" fill="url(#parchment-tone)"
             stroke="var(--charcoal-deep)" stroke-width="4"/>

    <!-- top banner -->
    <path class="banner banner--top" d="M80 110 Q304 0 528 110 L540 160 Q304 60 68 160 Z" fill="var(--charcoal)"/>
    <text class="brand-name" text-anchor="middle">
      <textPath href="#brand-arc" startOffset="50%">THISTLE &amp; RYE</textPath>
    </text>

    <!-- bowl illustration -->
    <rect class="bowl-illustration" x="218" y="120" width="150" height="104" rx="40"
          fill="url(#bowl-tone)" opacity="0.7" role="img" aria-label="Sketched bowl of soup illustration"/>

    <!-- product name -->
    <text class="product-title" x="304" y="362" font-size="118" text-anchor="middle"
          textLength="516" lengthAdjust="spacingAndGlyphs">CHICKEN</text>
    <text class="product-title" x="304" y="478" font-size="96" text-anchor="middle"
          textLength="360" lengthAdjust="spacingAndGlyphs">POT PIE</text>

    <!-- motto -->
    <rect class="motto-plate" x="104" y="510" width="402" height="48" fill="var(--charcoal)"/>
    <rect class="motto-plate" x="160" y="564" width="288" height="48" fill="var(--charcoal)"/>
    <text class="motto" x="305" y="549" text-anchor="middle" textLength="390" lengthAdjust="spacingAndGlyphs">SIMPLE SUPPERS,</text>
    <text class="motto" x="304" y="603" text-anchor="middle" textLength="270" lengthAdjust="spacingAndGlyphs">EVERY DAY</text>

    <!-- bottom banner -->
    <path class="banner banner--bottom" d="M70 640 Q300 690 540 630 L548 734 L60 734 Z" fill="var(--charcoal)"/>
    <text class="weight" text-anchor="middle">
      <textPath href="#weight-arc" startOffset="50%">WEIGHT: 40G</textPath>
    </text>
  </svg>
</main>
</body>
</html>
```